Bref créative
PeakMotion Chiropractic stationary
Simple
PeakMotion Chiropractic Inc.
Colin R Dembry D.C.
1148 Harmon Way Suite 12
Greenfield, IN 46273
(inside Norrin Callow Fitness Center)
dembrydc@qvmail.example
will ad later
Try to implement this tag line
"work hard, play hard, safe guard"
place for next appointment
can upload different formats, just let me know

```html
<!DOCTYPE html>
<html lang="en">
<head>
<meta charset="utf-8">
<title>PeakMotion Chiropractic Stationery</title>
<link rel="stylesheet" href="https://fonts.googleapis.com/css2?family=Roboto:wght@400;700;900&display=swap">
<style>
  :root {
    --blue: #1e4fa6;
    --blue-deep: #122f78;
    --blue-light: #3f74c9;
    --red: #e1262c;
    --ink: #333a45;
    --line: #9aa3b0;
    --paper: #ffffff;
    --stage: #ffffff;
  }
  * { box-sizing: border-box; margin: 0; padding: 0; }
  html, body { width: 1200px; height: 653px; overflow: hidden; background: var(--stage); }
  body { font-family: "Roboto", Arial, sans-serif; color: var(--ink); }
  .canvas { position: relative; width: 1200px; height: 653px; overflow: hidden; }

  .sheet, .envelope, .card {
    position: absolute; background: var(--paper); overflow: hidden;
    box-shadow: 0 2px 6px rgba(0,0,0,.18);
  }
  .brand { display: flex; align-items: center; gap: 6px; white-space: nowrap; }
  .brand-dot { width: 22px; height: 22px; border-radius: 50%; background: var(--red); flex: none; }
  .brand-name { font-weight: 900; color: var(--blue); font-size: 17px; line-height: 1; letter-spacing: .2px; }

  .band { position: absolute; left: 0; bottom: 0; width: 100%; }
  .band svg { display: block; width: 100%; height: 100%; }
  .band-text {
    position: absolute; left: 20px; bottom: 12px; color: #fff;
    font-size: 6.5px; line-height: 1.45; white-space: nowrap;
  }
  .seal { position: absolute; border-radius: 50%; background: rgba(255,255,255,.22); }

  /* fax sheet */
  .fax { left: 48px; top: 60px; width: 427px; height: 535px; }
  .fax .brand { position: absolute; left: 26px; top: 30px; }
  .fax-fields {
    position: absolute; left: 40px; top: 108px; width: 348px;
    display: grid; grid-template-columns: 1fr 1fr; column-gap: 36px; row-gap: 12px;
  }
  .field { display: flex; align-items: flex-end; font-size: 7.5px; font-weight: 700; }
  .field span { width: 34px; flex: none; }
  .field i { flex: 1; border-bottom: 1px solid var(--line); height: 9px; }
  .fax-checks {
    position: absolute; left: 40px; top: 222px; display: flex; gap: 18px;
    font-size: 7px; font-weight: 700; white-space: nowrap;
  }
  .check { display: flex; align-items: center; gap: 5px; }
  .check b { width: 8px; height: 8px; border: 1px solid var(--ink); }
  .fax .band { height: 80px; }

  /* letterhead */
  .letterhead { left: 492px; top: 60px; width: 432px; height: 535px; }
  .letterhead .brand { position: absolute; left: 16px; top: 30px; }
  .letterhead .band { height: 80px; }

  /* envelope */
  .envelope { left: 504px; top: 240px; width: 444px; height: 345px; }
  .flap { position: absolute; left: 0; top: 0; width: 100%; height: 80px; }
  .flap svg { display: block; width: 100%; height: 100%; }
  .flap-seal {
    position: absolute; left: 204px; top: 10px; width: 36px; height: 36px;
    border-radius: 50%; background: #fff; border: 3px solid var(--red);
  }
  .envelope .brand { position: absolute; left: 22px; top: 100px; }
  .envelope .brand-name { font-size: 19px; }
  .envelope-address {
    position: absolute; left: 24px; top: 210px; font-size: 6.5px; line-height: 1.5;
    color: var(--ink); white-space: nowrap;
  }
  .envelope .band { height: 78px; }

  /* business cards */
  .card { width: 144px; }
  .card-front { left: 984px; top: 271px; height: 60px; border: 1px solid #d7dbe2; }
  .card-front .brand { position: absolute; left: 6px; top: 8px; gap: 3px; }
  .card-front .brand-dot { width: 9px; height: 9px; }
  .card-front .brand-name { font-size: 7.5px; }
  .card-contact {
    position: absolute; right: 6px; top: 8px; text-align: right;
    font-size: 4.5px; line-height: 1.5; white-space: nowrap;
  }
  .card-contact strong { font-size: 5.5px; color: var(--blue); display: block; }
  .card-front .band { height: 16px; }
  .card-back {
    left: 984px; top: 386px; height: 82px;
    background: radial-gradient(circle at 30% 40%, var(--blue-light), var(--blue-deep));
  }
  .card-back .seal { left: 14px; top: 24px; width: 30px; height: 30px; background: #fff; border: 2px solid var(--red); }
  .tagline {
    position: absolute; left: 50px; top: 36px; color: #fff;
    font-size: 6px; font-weight: 700; white-space: nowrap;
  }
</style>
</head>
<body>
<main class="canvas">

  <section class="sheet fax" aria-label="Fax cover sheet">
    <div class="brand"><span class="brand-dot"></span><span class="brand-name">PeakMotion Chiropractic</span></div>
    <div class="fax-fields">
      <div class="field"><span>To:</span><i></i></div>
      <div class="field"><span>From:</span><i></i></div>
      <div class="field"><span>Fax:</span><i></i></div>
      <div class="field"><span>Pages:</span><i></i></div>
      <div class="field"><span>Phone:</span><i></i></div>
      <div class="field"><span>Date:</span><i></i></div>
      <div class="field"><span>Re:</span><i></i></div>
      <div class="field"><span>CC:</span><i></i></div>
    </div>
    <div class="fax-checks">
      <div class="check"><b></b>Urgent</div>
      <div class="check"><b></b>For Review</div>
      <div class="check"><b></b>Please Comment</div>
      <div class="check"><b></b>Please Reply</div>
    </div>
    <div class="band">
      <svg viewBox="0 0 427 80" preserveAspectRatio="none">
        <path d="M0 26 Q215 -6 427 14 L427 21 Q215 2 0 33Z" fill="var(--red)"/>
        <path d="M0 38 Q215 8 427 26 L427 80 L0 80Z" fill="var(--blue)"/>
      </svg>
      <span class="seal" style="right:18px;bottom:8px;width:32px;height:32px"></span>
      <p class="band-text">1148 Harmon Way Suite 12, Greenfield, IN 46273<br>(inside Norrin Callow Fitness Center)<br>Phone (317) 555-0142 Fax (317) 555-0143</p>
    </div>
  </section>

  <section class="sheet letterhead" aria-label="Letterhead">
    <div class="brand"><span class="brand-dot"></span><span class="brand-name">PeakMotion Chiropractic</span></div>
    <div class="band">
      <svg viewBox="0 0 432 80" preserveAspectRatio="none">
        <path d="M0 26 Q220 -6 432 14 L432 21 Q220 2 0 33Z" fill="var(--red)"/>
        <path d="M0 38 Q220 8 432 26 L432 80 L0 80Z" fill="var(--blue)"/>
      </svg>
    </div>
  </section>

  <section class="envelope" aria-label="Envelope">
    <div class="flap">
      <svg viewBox="0 0 444 80" preserveAspectRatio="none">
        <defs>
          <linearGradient id="flapBlue" x1="0" y1="0" x2="0" y2="1">
            <stop offset="0" stop-color="var(--blue-deep)"/>
            <stop offset="1" stop-color="var(--blue)"/>
          </linearGradient>
        </defs>
        <path d="M0 0 H444 V58 Q230 78 0 64Z" fill="url(#flapBlue)"/>
        <path d="M0 68 Q230 82 444 62 L444 66 Q230 88 0 73Z" fill="var(--red)"/>
      </svg>
      <span class="flap-seal"></span>
    </div>
    <div class="brand"><span class="brand-dot"></span><span class="brand-name">PeakMotion Chiropractic</span></div>
    <p class="envelope-address">1148 Harmon Way Suite 12, Greenfield, IN 46273<br>(inside Norrin Callow Fitness Center)<br>Phone (317) 555-0142 Fax (317) 555-0143</p>
    <div class="band">
      <svg viewBox="0 0 444 78" preserveAspectRatio="none">
        <path d="M0 24 Q230 -6 444 12 L444 19 Q230 2 0 31Z" fill="var(--red)"/>
        <path d="M0 36 Q230 8 444 24 L444 78 L0 78Z" fill="var(--blue)"/>
      </svg>
      <span class="seal" style="right:16px;bottom:8px;width:30px;height:30px"></span>
    </div>
  </section>

  <section class="card card-front" aria-label="Business card front">
    <div class="brand"><span class="brand-dot"></span><span class="brand-name">PeakMotion</span></div>
    <div class="card-contact">
      <strong>Colin R Dembry D.C.</strong>
      PeakMotion Chiropractic Inc.<br>
      dembrydc@qvmail.example
    </div>
    <div class="band">
      <svg viewBox="0 0 144 16" preserveAspectRatio="none">
        <path d="M0 5 Q75 -1 144 2 L144 4 Q75 1 0 7Z" fill="var(--red)"/>
        <path d="M0 8 Q75 2 144 5 L144 16 L0 16Z" fill="var(--blue)"/>
      </svg>
    </div>
  </section>

  <section class="card card-back" aria-label="Business card back">
    <span class="seal"></span>
    <p class="tagline">work hard, play hard, safe guard</p>
  </section>

</main>
</body>
</html>
```